TV Antenna Installation business needs a unique flyer

We need a simple but effective flyer design for our TV Aerial installation company based in Newcastle, NSW, Australia called Clearpeak TV & Aerial Svcs.
We are trying to target areas where there has been a new transmitter installed and most houses just require their aerial redirecting and tv's retuning.

Industry/Entity Type

Business

Requirements
Must have
• We would like the idea of a headline phrase such as " Poor TV reception……..now a thing from the past" or something similar & catchy.
Also "Did you know a new transmitter has been recently installed in your area, we can therefore now GUARANTEE 100% PERFECT PICTURE
Charges from only $95.
- Free 5 year warranty
- Free signal testing
- Free Onsite Quote
Phone 0452 736 205
Nice to have
• Other services include:

- New Installs
- Extra Points & repairs
- TV wall mounting/Home Cinema
- Pull down tall masts

Modern tv picture, see example uploaded

```html
<!DOCTYPE html>
<html lang="en">
<head>
<meta charset="utf-8">
<title>Clearpeak TV &amp; Aerial Svcs – Flyer</title>
<link rel="stylesheet" href="https://fonts.googleapis.com/css2?family=Montserrat:ital,wght@0,700;0,800;1,800&family=Open+Sans:wght@600;700&family=Oswald:wght@700&display=swap">
<style>
  :root {
    --night: #0b0f1e;
    --glow: #fffdf4;
    --ember: #c8401a;
    --maroon: #5a0b1c;
    --wine: #2a0610;
    --alert-red: #d4141c;
    --white: #ffffff;
    --sky-blue: #2aa3d6;
    --deep-blue: #0d5f9a;
    --ice-blue: #7fd8ff;
    --ink-navy: #0b2a48;
    --ghost: rgba(255, 255, 255, 0.13);
  }
  * { box-sizing: border-box; margin: 0; padding: 0; }
  html, body { width: 848px; height: 1200px; overflow: hidden; background: var(--night); }
  .flyer {
    position: relative;
    width: 848px;
    height: 1200px;
    overflow: hidden;
    font-family: "Montserrat", sans-serif;
    background:
      radial-gradient(ellipse 520px 380px at 50% 52%, var(--glow) 0%, rgba(255,250,235,0.95) 45%, rgba(255,240,220,0) 100%),
      linear-gradient(180deg, var(--night) 0%, #1b2338 18%, #d9d4cc 32%, #f4efe6 55%, #e8a27a 70%, var(--ember) 76%, var(--maroon) 86%, var(--wine) 100%);
  }
  .art { position: absolute; }
  .art--old-tv {
    left: 36px; top: 258px; width: 246px; height: 156px;
    border-radius: 14px;
    background: linear-gradient(135deg, #2c2c2c, #0e0e0e);
    transform: rotate(-4deg);
  }
  .art--modern-tv {
    left: 438px; top: 84px; width: 366px; height: 330px;
    background: linear-gradient(160deg, #3a4660 0%, #2e5a2a 55%, #101010 100%);
    border-radius: 6px;
  }
  .headline { position: absolute; left: 0; width: 100%; text-align: center; }
  .headline__lead {
    top: 76px; font-family: "Oswald", sans-serif; font-size: 25px; letter-spacing: 1px;
    color: var(--alert-red); text-shadow: 0 0 6px rgba(255,255,255,0.6);
  }
  .headline__main {
    top: 100px; font-family: "Oswald", sans-serif; font-size: 44px; letter-spacing: 1px;
    color: var(--alert-red); text-shadow: 0 0 8px rgba(255,255,255,0.7);
  }
  .brand-name {
    position: absolute; left: 0; top: 156px; width: 100%; text-align: center;
    font-weight: 800; font-size: 36px; line-height: 38px; color: var(--white);
    text-shadow: 0 2px 4px rgba(0,0,0,0.5);
  }
  .promise { position: absolute; left: 0; width: 100%; text-align: center;
    font-family: "Open Sans", sans-serif; font-weight: 700; line-height: 1; }
  .promise__top { top: 476px; font-size: 76px; color: var(--sky-blue); }
  .promise__big { top: 552px; font-size: 132px; color: var(--deep-blue); letter-spacing: -1px; }
  .promise__bottom { top: 676px; font-size: 98px; color: var(--deep-blue); }
  .perks { position: absolute; left: 214px; top: 796px; list-style: none; }
  .perks li {
    display: flex; align-items: center; height: 28px;
    font-family: "Open Sans", sans-serif; font-weight: 700; font-size: 20px;
    color: var(--deep-blue);
  }
  .perks li:nth-child(2) { padding-left: 14px; }
  .perks li:nth-child(3) { padding-left: 28px; }
  .perks svg { width: 26px; height: 22px; margin-right: 10px; }
  .ghost-name {
    position: absolute; left: 36px; width: 780px; font-weight: 800; font-size: 33px;
    color: var(--ghost); white-space: nowrap; overflow: hidden;
  }
  .notice { position: absolute; left: 0; width: 100%; text-align: center;
    font-style: italic; font-weight: 800; color: var(--white); }
  .notice__title { top: 906px; font-size: 30px; }
  .notice__body { top: 948px; font-size: 17px; line-height: 26px; }
  .price {
    position: absolute; left: 0; top: 1000px; width: 100%; text-align: center;
    font-style: italic; font-weight: 800; font-size: 56px; color: var(--ice-blue);
    text-shadow: 0 3px 0 var(--ink-navy), 0 0 10px rgba(0,0,0,0.5);
  }
  .phone {
    position: absolute; left: 0; top: 1096px; width: 100%; text-align: center;
    font-weight: 800; font-size: 42px; letter-spacing: 4px; color: var(--ice-blue);
    -webkit-text-stroke: 1.5px var(--ink-navy);
  }
</style>
</head>
<body>
<main class="flyer">
  <div class="art art--modern-tv" role="img" aria-label="Modern flat-screen TV showing a football player"></div>
  <div class="art art--old-tv" role="img" aria-label="Old television with antenna showing colour test bars"></div>

  <p class="headline headline__lead">POOR TV RECEPTION...</p>
  <h1 class="headline headline__main">NOW A THING FROM THE PAST</h1>
  <p class="brand-name">CLEARPEAK TV<br>AND AERIAL SVCS</p>

  <h2 class="promise promise__top">100% PERFECT</h2>
  <p class="promise promise__big">PICTURE</p>
  <p class="promise promise__bottom">GUARANTEED</p>

  <ul class="perks">
    <li><svg viewBox="0 0 26 22"><path d="M2 12 L9 19 L24 3" fill="none" stroke="#2aa3d6" stroke-width="4" stroke-linecap="round"/></svg>FREE 5 YEAR WARRANTY</li>
    <li><svg viewBox="0 0 26 22"><path d="M2 12 L9 19 L24 3" fill="none" stroke="#2aa3d6" stroke-width="4" stroke-linecap="round"/></svg>FREE SIGNAL TESTING</li>
    <li><svg viewBox="0 0 26 22"><path d="M2 12 L9 19 L24 3" fill="none" stroke="#2aa3d6" stroke-width="4" stroke-linecap="round"/></svg>FREE ONSITE QUOTE</li>
  </ul>

  <p class="ghost-name" style="top:940px">CLEARPEAK TV AND AERIAL SVCS</p>
  <p class="ghost-name" style="top:976px">CLEARPEAK TV AND AERIAL SVCS</p>
  <p class="ghost-name" style="top:1012px">CLEARPEAK TV AND AERIAL SVCS</p>
  <p class="ghost-name" style="top:1046px">CLEARPEAK TV AND AERIAL SVCS</p>
  <p class="ghost-name" style="top:1080px">CLEARPEAK TV AND AERIAL SVCS</p>
  <p class="ghost-name" style="top:1114px">CLEARPEAK TV AND AERIAL SVCS</p>
  <p class="ghost-name" style="top:1148px">CLEARPEAK TV AND AERIAL SVCS</p>

  <p class="notice notice__title">DID YOU KNOW?</p>
  <p class="notice notice__body">A NEW TRANSMITTER HAS JUST BEEN INSTALLED IN YOUR AREA.<br>WE CAN THEREFORE NOW GUARANTEE 100% PERFECT PICTURE</p>

  <p class="price">CHARGES FROM ONLY $95.</p>
  <p class="phone">PHONE 0452 736 205</p>
</main>
</body>
</html>
```